KVT Calculator

We have a calculator already created however the design seems to be very boring and bland. The calculators goal is to show graphic designers, web development firms, pr agencies, marketing firms how much revenue they can potentially make by offering a managed social media solution to their clients.

We want a great designer to make the calculator appealing to our audience.

It is an amazing offer and opportunity however I do not believe the current design does it justice

you can view and play with calculator live at http://sandbox.plivoran.com/tkna/

```html
<!DOCTYPE html>
<html lang="en">
<head>
<meta charset="utf-8">
<title>Profit Calculator</title>
<link rel="stylesheet" href="https://fonts.googleapis.com/css2?family=Open+Sans:wght@400;600&display=swap">
<style>
  :root {
    --sky: #0598f2;
    --panel: #333333;
    --panel-edge: #f4f4f4;
    --ink: #111111;
    --label: #ffffff;
    --basic: #29a8e3;
    --pro: #f7931e;
    --enterprise: #39b54a;
    --knob: #1c1c1c;
    --tick: #6b0f12;
  }
  * { box-sizing: border-box; margin: 0; padding: 0; }
  html, body { width: 1200px; height: 800px; overflow: hidden; }
  body {
    background: var(--sky);
    font-family: "Open Sans", Arial, sans-serif;
    position: relative;
  }
  .panel {
    position: absolute; left: 81px; top: 208px; width: 1039px; height: 430px;
    background: var(--panel); border-radius: 4px;
    border-bottom: 2px solid var(--panel-edge);
  }
  .term {
    position: absolute; left: 121px; top: 163px; width: 116px; height: 474px;
    border: 2px solid #111; border-radius: 4px; overflow: hidden; background: #2b2b2b;
  }
  .term-title {
    height: 44px; color: #fff; font-size: 15.5px; letter-spacing: 1px;
    text-align: center; line-height: 44px; white-space: nowrap;
  }
  .term svg { display: block; }
  .row-label {
    position: absolute; left: 276px; color: var(--label);
    font-size: 16.5px; letter-spacing: 1.6px; transform: translateY(-50%); white-space: nowrap;
  }
  .row-rule { position: absolute; left: 276px; width: 221px; height: 1px; background: #e8e8e8; }
  .plan { position: absolute; top: 163px; height: 346px; }
  .plan-tab {
    height: 45px; color: #fff; font-size: 18.5px; letter-spacing: 3.2px;
    text-align: center; line-height: 45px; border-radius: 6px 6px 0 0; white-space: nowrap;
  }
  .plan--basic { left: 505px; width: 197px; }
  .plan--pro { left: 709px; width: 196px; }
  .plan--enterprise { left: 912px; width: 192px; }
  .plan--basic .plan-tab { background: var(--basic); border-top-left-radius: 45px; }
  .plan--pro .plan-tab { background: var(--pro); }
  .plan--enterprise .plan-tab { background: var(--enterprise); border-top-right-radius: 45px; }
  .plan-body {
    position: relative; height: 277px;
    background: linear-gradient(to bottom, #3a3a3a 0%, #d8d8d8 14%, #f4f4f4 24%, #d6d6d6 30%,
      #f6f6f6 45%, #dcdcdc 54%, #f4f4f4 64%, #d2d2d2 80%, #6a6a6a 92%, #3d3d3d 100%);
  }
  .plan-foot { height: 24px; border-radius: 0 0 4px 4px; }
  .plan--basic .plan-foot { background: var(--basic); }
  .plan--pro .plan-foot { background: var(--pro); }
  .plan--enterprise .plan-foot { background: var(--enterprise); }
  .cell {
    position: absolute; left: 0; right: 0; text-align: center;
    font-size: 18.5px; letter-spacing: 1.2px; color: var(--ink); transform: translateY(-50%);
  }
  .cell-rule { position: absolute; left: 10px; right: 14px; height: 2px; background: #111; }
  .step {
    position: absolute; width: 33px; height: 33px; border-radius: 50%;
    background: var(--knob); color: #fff; font-size: 26px; line-height: 31px;
    text-align: center; transform: translate(-50%, -50%); border: 1px solid #777;
  }
  .total {
    position: absolute; left: 238px; top: 560px; width: 870px; height: 50px;
    background: linear-gradient(to right, #5a5a5a 0%, #f2f2f2 9%, #fafafa 55%, #e4e4e4 85%, #3a3a3a 100%);
    font-size: 35px; color: var(--ink); line-height: 50px; padding-left: 39px;
    letter-spacing: 1.3px; white-space: nowrap;
  }
</style>
</head>
<body>
  <div class="panel"></div>

  <div class="term">
    <div class="term-title">TERM (YRS)</div>
    <svg width="112" height="426" viewBox="0 0 112 426" aria-label="Term slider set to year 4">
      <defs>
        <linearGradient id="metal" x1="0" x2="1">
          <stop offset="0" stop-color="#9a9a9a"/><stop offset=".45" stop-color="#f2f2f2"/>
          <stop offset=".55" stop-color="#f8f8f8"/><stop offset="1" stop-color="#8e8e8e"/>
        </linearGradient>
        <pattern id="grid" width="8" height="8" patternUnits="userSpaceOnUse">
          <path d="M8 0H0V8" fill="none" stroke="#000" stroke-opacity=".08"/>
        </pattern>
        <linearGradient id="track" x1="0" x2="1">
          <stop offset="0" stop-color="#bcbcbc"/><stop offset=".5" stop-color="#f4f4f4"/><stop offset="1" stop-color="#bcbcbc"/>
        </linearGradient>
        <linearGradient id="red" x1="0" x2="1">
          <stop offset="0" stop-color="#b5161a"/><stop offset=".5" stop-color="#ffb3b3"/><stop offset="1" stop-color="#b5161a"/>
        </linearGradient>
        <radialGradient id="knob" cx=".4" cy=".35" r=".7">
          <stop offset="0" stop-color="#9a9a9a"/><stop offset=".6" stop-color="#555"/><stop offset="1" stop-color="#222"/>
        </radialGradient>
      </defs>
      <rect width="112" height="426" fill="url(#metal)"/>
      <rect width="112" height="426" fill="url(#grid)"/>
      <g stroke="var(--tick)" stroke-width="2">
        <path d="M25 39h62M25 75h62M25 111h62M25 147h62M25 183h62M25 219h62M25 255h62M25 291h62M25 327h62M25 363h62"/>
      </g>
      <rect x="47" y="32" width="18" height="360" rx="9" fill="url(#track)" stroke="#999"/>
      <rect x="47" y="258" width="18" height="134" rx="9" fill="url(#red)"/>
      <circle cx="56" cy="257" r="25" fill="url(#knob)" stroke="#222"/>
      <path d="M49 262l7-9 7 9" fill="none" stroke="#ddd" stroke-width="2"/>
    </svg>
  </div>

  <div class="row-label" style="top:247px">Clients per month:</div>
  <div class="row-rule" style="top:284px"></div>
  <div class="row-label" style="top:313px">You Cost:</div>
  <div class="row-rule" style="top:347px"></div>
  <div class="row-label" style="top:387px">Your client pays:</div>
  <div class="row-rule" style="top:425px"></div>
  <div class="row-label" style="top:463px">Monthly profit (year 4):</div>

  <div class="plan plan--basic">
    <div class="plan-tab">BASIC</div>
    <div class="plan-body">
      <span class="step" style="left:21px;top:36px">-</span>
      <div class="cell" style="top:38px">1</div>
      <span class="step" style="left:174px;top:36px">+</span>
      <div class="cell-rule" style="top:74px"></div>
      <div class="cell" style="top:103px">$197</div>
      <div class="cell-rule" style="top:138px"></div>
      <span class="step" style="left:21px;top:178px">-</span>
      <div class="cell" style="top:178px">$297</div>
      <span class="step" style="left:174px;top:178px">+</span>
      <div class="cell-rule" style="top:215px"></div>
      <div class="cell" style="top:255px">$4,800</div>
    </div>
    <div class="plan-foot"></div>
  </div>

  <div class="plan plan--pro">
    <div class="plan-tab">PRO</div>
    <div class="plan-body">
      <span class="step" style="left:21px;top:36px">-</span>
      <div class="cell" style="top:38px">3</div>
      <span class="step" style="left:174px;top:36px">+</span>
      <div class="cell-rule" style="top:74px"></div>
      <div class="cell" style="top:103px">$297</div>
      <div class="cell-rule" style="top:138px"></div>
      <span class="step" style="left:21px;top:178px">-</span>
      <div class="cell" style="top:178px">$347</div>
      <span class="step" style="left:174px;top:178px">+</span>
      <div class="cell-rule" style="top:215px"></div>
      <div class="cell" style="top:255px">$7,200</div>
    </div>
    <div class="plan-foot"></div>
  </div>

  <div class="plan plan--enterprise">
    <div class="plan-tab">ENTERPRISE</div>
    <div class="plan-body">
      <span class="step" style="left:20px;top:36px">-</span>
      <div class="cell" style="top:38px">2</div>
      <span class="step" style="left:174px;top:36px">+</span>
      <div class="cell-rule" style="top:74px"></div>
      <div class="cell" style="top:103px">$2500</div>
      <div class="cell-rule" style="top:138px"></div>
      <span class="step" style="left:20px;top:178px">-</span>
      <div class="cell" style="top:178px">$4000</div>
      <span class="step" style="left:174px;top:178px">+</span>
      <div class="cell-rule" style="top:215px"></div>
      <div class="cell" style="top:255px">$144,000</div>
    </div>
    <div class="plan-foot"></div>
  </div>

  <div class="total">Monthly profit by the end of year 4: $156,000</div>
</body>
</html>
```